Therapy Services & Training

I provide counseling/therapy to individuals and families. I also travel the country and provide training at conferences.
I would like to see a card which takes my company name and design a logo using the letters "HWAE".
Target Market(s)
Therapists, non-profit organizations, clients looking for therapy
Industry/Entity Type
Training
Contact Information for Business Card
Harborview Wellness Advising & Education LLC
Delia Marsh, M.S.W., LCSW
Clinical Therapist & Trainer
Providing clinical therapy services to individuals, families, couples & children. We also provide life coaching and crisis training.
counselordelia@mailbrook.net
www.harborviewwellnessadvising.com
(555) 214-3092
Brookhollow, IL 60999
(BACK SIDE OF CARD)
We are certified by the Ongoing Professional Lawyer Studies (OPLS) Council of the Prairie High Tribunal to provide Continuing Legal Education (CLE) credits to Illinois attorneys. Call about what courses we offer! (555) 214-3092

```html
<!DOCTYPE html>
<html lang="en">
<head>
<meta charset="utf-8">
<title>HWAE Business Card</title>
<link rel="stylesheet" href="https://fonts.googleapis.com/css2?family=Tinos:ital,wght@0,400;0,700;1,700&family=Poppins:wght@600;700&family=Didact+Gothic&family=Lobster+Two:ital,wght@1,700&display=swap">
<style>
  :root {
    --board-tan: #c8b98c;
    --board-sage: #a5a77c;
    --panel-cream: #f3efbd;
    --card-white: #ffffff;
    --ink: #111111;
    --deep-teal: #0f4d63;
    --script-teal: #1d6a86;
    --rule-blue: #8fb9cb;
    --mist-blue: #dfe9f4;
    --faint-blue: #c3d9e4;
  }
  * { margin: 0; padding: 0; box-sizing: border-box; }
  html, body { width: 927px; height: 1200px; overflow: hidden; }
  body { position: relative; font-family: "Didact Gothic", sans-serif; color: var(--ink); }

  .board-backdrop {
    position: absolute; inset: 0;
    background: radial-gradient(circle at 40% 45%, var(--board-tan), var(--board-sage));
  }

  .sheet-title {
    position: absolute; left: 0; top: 18px; width: 645px; height: 84px;
    background: rgba(243, 239, 189, 0.85);
    font-family: "Tinos", serif; font-weight: 400; font-size: 56px; line-height: 84px;
    padding-left: 25px; color: var(--ink);
  }

  .pieces-panel {
    position: absolute; left: 36px; top: 133px; width: 836px; height: 229px;
    background: rgba(243, 239, 189, 0.92);
  }
  .pieces-label {
    position: absolute; left: 19px; top: 16px;
    font-family: "Tinos", serif; font-weight: 700; font-size: 22px;
  }
  .piece {
    position: absolute; top: 95px; display: flex; align-items: center; gap: 14px;
    font-family: "Poppins", sans-serif; font-weight: 700; font-size: 58px; line-height: 1; color: var(--ink);
  }
  .piece-wordmark { left: 28px; }
  .piece-mark { left: 270px; }
  .piece-mark .dot { width: 120px; height: 120px; margin-top: -30px; }
  .piece-lockup { left: 550px; }
  .dot { display: block; border-radius: 50%; background: var(--ink); flex: none; }
  .piece-lockup .dot { width: 50px; height: 50px; }

  .side-label {
    position: absolute; font-family: "Tinos", serif; font-size: 44px; color: var(--ink);
    transform: translate(-50%, -50%) rotate(-90deg); white-space: nowrap;
  }
  .side-front { left: 116px; top: 560px; }
  .side-back { left: 116px; top: 948px; }

  .card { position: absolute; background: var(--card-white); overflow: hidden; }
  .card-front { left: 207px; top: 412px; width: 542px; height: 317px; }
  .card-back { left: 202px; top: 788px; width: 551px; height: 322px; }

  .faint-name {
    position: absolute; font-family: "Poppins", sans-serif; font-weight: 700; line-height: 1;
    white-space: nowrap;
  }
  .card-front .faint-name { left: 120px; top: 160px; font-size: 118px; color: var(--mist-blue); }
  .card-back .faint-name { left: 190px; top: 130px; font-size: 74px; color: var(--faint-blue); }

  .front-brand {
    position: absolute; left: 22px; top: 28px; display: flex; align-items: center; gap: 8px;
    font-family: "Poppins", sans-serif; font-weight: 700; font-size: 36px; line-height: 1; color: var(--deep-teal);
  }
  .front-brand .dot { width: 22px; height: 22px; background: var(--deep-teal); }

  .top-rule { position: absolute; left: 188px; right: 0; top: 59px; height: 6px; background: var(--rule-blue); }

  .company-name {
    position: absolute; right: 10px; top: 34px; width: 340px; text-align: center;
    font-family: "Lobster Two", cursive; font-style: italic; font-weight: 700;
    font-size: 20px; line-height: 30px; color: var(--script-teal);
  }

  .practitioner {
    position: absolute; left: 95px; top: 115px; width: 350px; text-align: center;
    font-family: "Poppins", sans-serif; font-weight: 700; font-size: 20px; line-height: 1; color: var(--deep-teal);
    padding-bottom: 5px; border-bottom: 4px solid var(--rule-blue);
  }

  .services {
    position: absolute; left: 25px; top: 156px; white-space: nowrap;
    font-size: 14.5px; line-height: 19.5px; color: var(--ink);
  }

  .contact {
    position: absolute; right: 26px; top: 238px; text-align: right; list-style: none;
    font-family: "Poppins", sans-serif; font-weight: 600; font-size: 13.5px; line-height: 19.5px; color: var(--deep-teal);
  }

  .back-rule { position: absolute; left: 0; right: 0; top: 55px; height: 8px; background: var(--rule-blue); }

  .certification {
    position: absolute; left: 0; right: 0; top: 74px; text-align: center;
    font-size: 16.5px; line-height: 24px; color: var(--ink);
  }

  .call-out {
    position: absolute; left: 0; right: 0; top: 210px; text-align: center;
    font-family: "Poppins", sans-serif; font-weight: 700; font-size: 21px; line-height: 30px; color: var(--deep-teal);
  }

  .presentation-note {
    position: absolute; left: 0; right: 0; top: 1160px; text-align: center;
    font-family: "Tinos", serif; font-weight: 700; font-style: italic; font-size: 30px; color: var(--ink);
  }
</style>
</head>
<body>
  <div class="board-backdrop" role="img" aria-label="Tan presentation board with a sage damask flourish pattern"></div>

  <h1 class="sheet-title">HWAE Business Card</h1>

  <section class="pieces-panel">
    <h2 class="pieces-label">Logo &amp; Pieces</h2>
    <div class="piece piece-wordmark">HWAE</div>
    <div class="piece piece-mark"><span class="dot"></span></div>
    <div class="piece piece-lockup"><span class="dot"></span>HWAE</div>
  </section>

  <div class="side-label side-front">Front Side</div>
  <article class="card card-front">
    <div class="faint-name" aria-hidden="true">HWAE</div>
    <div class="front-brand"><span class="dot"></span>HWAE</div>
    <div class="top-rule"></div>
    <p class="company-name">Harborview Wellness Advising &amp;<br>Education LLC</p>
    <h3 class="practitioner">Delia Marsh, M.S.W., LCSW</h3>
    <p class="services">Clinical Therapist &amp; Trainer Providing<br>clinical therapy services to individuals,<br>families, couples &amp; children. We also<br>provide life coaching and crisis<br>training.</p>
    <ul class="contact">
      <li>counselordelia@mailbrook.net</li>
      <li>www.harborviewwellnessadvising.com</li>
      <li>(555) 214-3092 Brookhollow, IL 60999</li>
    </ul>
  </article>

  <div class="side-label side-back">Back Side</div>
  <article class="card card-back">
    <div class="back-rule"></div>
    <div class="faint-name" aria-hidden="true">HWAE</div>
    <p class="certification">We are certified by the Ongoing Professional<br>Lawyer Studies (OPLS) Council of the Prairie<br>High Tribunal to provide Continuing Legal<br>Education (CLE) credits to Illinois attorneys.</p>
    <p class="call-out">Call about what courses we<br>offer!<br>(555) 214-3092</p>
  </article>

  <p class="presentation-note">Please Note: Background is not part of the design....</p>
</body>
</html>
```